gracefulgemstore.com.au needs a new web design!

We are after a refurbished web design. gracefulgemstore.com.au is an online jewellery store - it represents a brand that is elegant, graceful and superior in quality.

We have colours that we like but are open to new colour schemes. Our favourite colours are teal and cherry (see attached colour story). We also like simple designs with lots of white space.

A website which we love the layout and design is www.velmora.com.au please try and design in a similar fashion.

We require three important pages:

- Home page
- Tiled product category Page (eg. earrings, see current website)
- Single Product Page.

Please be aware we are limited to the current Content Management System for our website so using similiar (but not limited too) layout would be helpful for the lonely developer (me).

Our designer should provide (at least) photoshop files for our disposal with category headings etc being able to be edited as we add or change new product categories.

We have plans to get large photos of models for the home page in the future, but should also be available for large photos of jewellery. Basically we believe photos are essential to sell our product, so please don't be afraid to incorporate some dummy photos into your design. Especially the home page!

We also offer free shipping Australia Wide, please incorporate this into the home page, product and category pages, it needs to show the visitor that it is specifically Free Australian wide shipping.

Other stuff we need:

A cool shipping info button/box (see current single product page)
Some Social networking buttons/boxes for Chatterly and quipster for possible use on home page.

please email oliver@gracefulgemstore.com.au if you have any questions.

Many thanks and we look forward to reviewing your designs.
Updates

Thankyou all for your designs, I have messaged 4 designs which are the front runners. some have been reuqested to make slight adjustments, others have been asked to submit the other pages as per brief.

Cheers,

Oliver

Target Market(s)

Ladies in Australia between the ages of 25 and 55

Industry/Entity Type

Shipping

Requirements
Must have
• Hovers, actions and transitions and potential drop downs
Should not have
• Norvane motion.

```html
<!DOCTYPE html>
<html lang="en">
<head>
<meta charset="utf-8">
<title>Heart Locket Charm in sterling silver – Graceful Gem Store</title>
<link rel="stylesheet" href="https://fonts.googleapis.com/css2?family=PT+Sans:wght@400;700&family=Open+Sans:wght@400;600;700&display=swap">
<style>
:root{
  --page:#ebebe9;
  --panel:#f7f7f5;
  --white:#ffffff;
  --teal:#79d1d9;
  --cherry:#e06464;
  --cherry-text:#d9232d;
  --ink:#2f2f2f;
  --grey:#777777;
  --soft:#a5a5a5;
  --line:#dcdcdc;
  --tab:#ecece8;
  --footer:#474747;
  --footer-text:#f2f2f2;
  --footer-head:#c9c9c9;
  --dark-btn:#3b3b3b;
}
*{box-sizing:border-box;margin:0;padding:0}
html,body{width:1183px;height:1200px;overflow:hidden}
body{background:var(--page);font-family:"Open Sans",sans-serif;color:var(--ink);position:relative}
a{color:inherit;text-decoration:none;transition:color .2s,background .2s}
.abs{position:absolute}

.sheet{position:absolute;left:121px;top:0;width:934px;height:961px;background:var(--panel)}

/* header */
.logo{left:136px;top:44px;font-family:"PT Sans",sans-serif;font-size:37px;color:#2b2b2b;letter-spacing:-1px;font-weight:400}
.bag{right:140px;top:26px;text-align:right}
.bag-title{display:flex;align-items:center;justify-content:flex-end;gap:6px;font-family:"PT Sans",sans-serif;font-size:15px;color:#3a3a3a;letter-spacing:.3px}
.bag-icon{width:30px;height:27px}
.bag-total{font-family:"PT Sans",sans-serif;font-size:12px;color:#8a7a52;margin-top:4px}
.bag-actions{display:flex;gap:4px;justify-content:flex-end;margin-top:9px}
.bag-actions a{font-family:"PT Sans",sans-serif;font-size:12px;letter-spacing:.4px;padding:2px 10px;height:20px}
.btn-view{background:#d9d9d9;color:#333}
.btn-checkout{background:var(--dark-btn);color:#fff}
.bag-actions a:hover{background:var(--cherry);color:#fff}

.main-nav{left:136px;top:118px;width:907px;height:23px;background:var(--teal);display:flex;padding-left:9px}
.main-nav a{font-family:"PT Sans",sans-serif;font-weight:700;font-size:11px;color:#fff;letter-spacing:.3px;line-height:23px;margin-right:29px}
.main-nav a:hover{color:var(--ink)}
.sub-nav{left:136px;top:143px;width:907px;height:27px;background:#f1f1ed;display:flex;align-items:center;padding-left:9px}
.sub-nav a{font-size:9.5px;letter-spacing:.2px;margin-right:11px;color:#333}
.sub-nav a:hover{color:var(--cherry)}
.search{position:absolute;right:4px;top:5px;display:flex;gap:4px}
.search input{width:150px;height:17px;border:1px solid #ddd;background:#fff}
.search button{height:17px;background:var(--cherry);color:#fff;border:0;font-size:10px;padding:0 6px;font-family:"Open Sans",sans-serif}

/* content */
.content{left:136px;top:172px;width:907px;height:778px;background:var(--white)}
.crumbs{left:145px;top:178px;font-size:9.5px;color:var(--soft)}
.hero{left:175px;top:240px;width:300px;height:290px;border-radius:50%;background:radial-gradient(circle at 50% 48%,#7fd0dc 0,#9fdde6 35%,#e4f2f4 58%,#ffffff 72%)}
.thumb{top:557px;width:80px;height:80px;border:1px solid #ddd;background:#fff;padding:10px}
.thumb span{display:block;width:100%;height:100%;border-radius:50%}
.thumb-a span{background:radial-gradient(circle,#f2f4f5 0,#cfd5d8 60%,#fff 75%)}
.thumb-b span{background:radial-gradient(circle,#7fd0dc 0,#b5e4ea 55%,#fff 75%)}
.enlarge{left:145px;top:648px;font-size:9.5px;color:var(--soft)}

.product-title{left:513px;top:199px;font-family:"PT Sans",sans-serif;font-size:15px;color:#222}
.delivery{left:513px;top:218px;font-size:11px;color:var(--grey)}
.price{left:512px;top:243px;font-family:"Open Sans",sans-serif;font-weight:700;font-size:26px;color:#2a2a2a}
.stock{left:513px;top:275px;font-size:11px;color:var(--grey)}
.add-basket{left:510px;top:307px;width:149px;height:37px;background:var(--cherry);color:#fff;font-family:"Open Sans",sans-serif;font-size:14px;line-height:37px;text-align:center}
.add-basket:hover{background:#c84b4b}

.tabs{left:510px;top:368px;width:440px;display:flex;gap:4px}
.tabs span{flex:1;height:23px;background:var(--tab);font-size:11px;color:#777;text-align:center;line-height:24px}
.tabs .on{background:#e4e4df;color:#666}
.tab-body{left:510px;top:391px;width:440px;height:144px;border:1px solid #cfcfcf;padding:15px 12px;font-size:11px;line-height:14px;color:#555}

.actions{left:510px;top:544px;width:440px;display:flex;justify-content:space-between}
.actions a{width:140px;height:24px;background:#e4e4e1;font-size:11px;color:#777;text-align:center;line-height:24px}
.actions a:hover{background:var(--teal);color:#fff}

.social{left:510px;top:582px;display:flex;align-items:center;gap:6px;font-size:9.5px;color:#333}
.like{border:1px solid #c9d3e6;background:#eef2f8;height:21px;padding:0 6px;display:flex;align-items:center;gap:3px;color:#3b5287;font-size:10px}
.sq{display:inline-block;width:11px;height:11px;background:#4a6499}
.quip{left:834px;top:582px;display:flex;gap:3px;align-items:center}
.quip-btn{border:1px solid #cbd8e0;background:#eaf2f7;height:19px;padding:0 5px;font-size:10px;font-weight:700;color:#2f4f66;display:flex;align-items:center;gap:3px}
.quip-btn i{width:9px;height:9px;border-radius:50%;background:#4aa3d8;display:inline-block}
.count{border:1px solid #bbb;height:19px;width:15px;font-size:9px;text-align:center;line-height:17px;background:#fff}

.related-head{left:145px;top:688px;font-family:"Open Sans",sans-serif;font-weight:600;font-size:12px;color:#2a2a2a}
.related-rule{left:145px;top:707px;width:892px;height:1px;background:#e6e6e6}
.grid{left:147px;top:722px;display:flex;gap:10px}
.card{width:128px;font-size:10px;color:#666;line-height:11.5px}
.card .pic{width:128px;height:128px;background:linear-gradient(135deg,#cfcfcf,#bdbdbd);margin-bottom:19px}
.card .name{height:34px;white-space:nowrap}
.card .rrp{color:var(--cherry-text);font-size:10px}
.card .now{font-family:"Open Sans",sans-serif;font-weight:700;font-size:16px;color:#707070;margin-top:2px;line-height:18px}
.card:hover .now{color:var(--cherry)}

/* footer */
.footer{left:0;top:984px;width:1183px;height:216px;background:var(--footer);color:var(--footer-text)}
.f-col{position:absolute;top:24px}
.f-col h4{font-family:"PT Sans",sans-serif;font-weight:700;font-size:11px;letter-spacing:.3px;color:var(--footer-head);margin-bottom:14px}
.f-col p,.f-col li{font-size:9px;line-height:12px;list-style:none}
.f-col b{font-weight:700}
.divider{position:absolute;top:56px;width:1px;height:146px;background:#5c5c5c}
.links{display:flex;gap:68px}
.news{display:flex;gap:4px}
.news input{width:214px;height:21px;border:1px solid #ccc;background:#fff;font-family:"Open Sans",sans-serif;font-size:11px;color:#777;padding-left:4px}
.news button{width:24px;height:21px;border:0;background:#8a8a8a}
.net{display:flex;gap:10px;margin-top:11px}
.net span{display:flex;align-items:center;gap:4px;font-size:11px;color:#eee;height:30px;border:2px solid #ddd;border-radius:4px;padding:0 6px}
.net i{width:8px;height:8px;background:#ddd;display:inline-block}
.pay{display:grid;grid-template-columns:repeat(4,auto);gap:10px 18px;margin-top:18px;font-family:"PT Sans",sans-serif;font-size:12px;font-weight:700;color:#bdbdbd;justify-content:start;align-items:center}
.badge{width:48px;height:18px;border-radius:3px;background:#6a6a6a}
</style>
</head>
<body>
<div class="sheet" role="img" aria-label="Light page backdrop"></div>

<header>
  <div class="abs logo">GRACEFUL GEM STORE</div>
  <div class="abs bag">
    <div class="bag-title">
      <svg class="bag-icon" viewBox="0 0 30 27"><path d="M4 7h22l-2 19H6z" fill="#2f2f2f"/><path d="M10 9V5a5 5 0 0 1 10 0v4" fill="none" stroke="#2f2f2f" stroke-width="2"/></svg>
      MY SHOPPING BAG
    </div>
    <div class="bag-total">$0.00 - Items (0)</div>
    <div class="bag-actions"><a class="btn-view" href="#">VIEW BAG</a><a class="btn-checkout" href="#">CHECKOUT</a></div>
  </div>
  <nav class="abs main-nav">
    <a href="#">ENGAGEMENT</a><a href="#">JEWELLERY</a><a href="#">DIAMONDS</a><a href="#">DESIGNERS</a><a href="#">ACCESSORIES</a>
  </nav>
  <nav class="abs sub-nav">
    <a href="#">HOME</a><a href="#">ABOUT US</a><a href="#">MY WISHLIST</a><a href="#">CONTACT US</a><a href="#">MY ACCOUNT</a>
    <form class="search"><input type="text" aria-label="Search"><button type="button">» Go</button></form>
  </nav>
</header>

<main>
  <div class="abs content"></div>
  <div class="abs crumbs">Home - Jewellery - Charms</div>

  <div class="abs hero" role="img" aria-label="Open heart locket in sterling silver with turquoise lining"></div>
  <div class="abs thumb thumb-a" style="left:145px" role="img" aria-label="Closed heart locket"><span></span></div>
  <div class="abs thumb thumb-b" style="left:230px" role="img" aria-label="Open heart locket"><span></span></div>
  <div class="abs enlarge">Click to enlarge images</div>

  <h1 class="abs product-title">Heart Locket Charm in sterling silver</h1>
  <div class="abs delivery">Free AU Delivery</div>
  <div class="abs price">$305.00</div>
  <div class="abs stock">Item in Stock &nbsp;|&nbsp; Usually dispatched within 48 hours</div>
  <a class="abs add-basket" href="#">ADD TO BASKET <small>›</small></a>

  <div class="abs tabs"><span class="on">Product Details</span><span>Delivery &amp; Returns</span><span>Rating</span></div>
  <div class="abs tab-body">Wear cherished photos close to your heart.<br>Locket in sterling silver. Size small. On a chain.<br>Locket and chain sold separately.</div>

  <div class="abs actions"><a href="#">Email a friend</a><a href="#">Ask a question</a><a href="#">Add to wish list</a></div>

  <div class="abs social">
    <span class="like">Like</span><span class="sq"></span>Be the first of your friends to like this.
  </div>
  <div class="abs quip"><span class="quip-btn"><i></i>Quip</span><span class="count">0</span></div>

  <h2 class="abs related-head">You may also be interested in:</h2>
  <div class="abs related-rule"></div>
  <div class="abs grid">
    <div class="card"><div class="pic" role="img" aria-label="Sterling silver hoop earrings"></div><div class="name">Sterling Silver Hoop Earrings</div><div class="rrp">RRP: $99.00 AUD</div><div class="now">$69.00 AUD</div></div>
    <div class="card"><div class="pic" role="img" aria-label="Hoop earrings with diamond insert"></div><div class="name">Sterling Silver Hoop Earrings<br>with dimond insert</div><div class="rrp">RRP: $89.00 AUD</div><div class="now">$49.00 AUD</div></div>
    <div class="card"><div class="pic" role="img" aria-label="Thick to thin hoop earrings"></div><div class="name">Sterling Silver Hoop Earrings<br>thick to thin</div><div class="rrp">RRP: $59.00 AUD</div><div class="now">$29.00 AUD</div></div>
    <div class="card"><div class="pic" role="img" aria-label="Twin loop hoop earrings"></div><div class="name">Sterling Silver Hoop Earrings<br>Twin loop</div><div class="rrp">RRP: $79.00 AUD</div><div class="now">$39.00 AUD</div></div>
    <div class="card"><div class="pic" role="img" aria-label="Long dangle earrings with flower"></div><div class="name">Sterling Silver Earrings<br>Long dangle with flower</div><div class="rrp">RRP: $64.00 AUD</div><div class="now">$24.00 AUD</div></div>
    <div class="card"><div class="pic" role="img" aria-label="Silver chain bracelet with heart tag"></div><div class="name">Sterling Silver Bracelet</div><div class="rrp">RRP: $179.00 AUD</div><div class="now">$139.00 AUD</div></div>
  </div>
</main>

<footer class="abs footer">
  <div class="f-col" style="left:136px">
    <h4>CONTACT US</h4>
    <p>Street<br>Town<br>Country</p>
    <p style="margin-top:24px"><b>Tel:</b> 01642 xxxxxx<br><b>Mail:</b> oliver@gracefulgemstore.com.au</p>
    <p style="margin-top:12px"><b>Opening Hours</b><br>Monday to Friday / 10am - 5pm<br>Saturday 9am - 5pm</p>
  </div>
  <div class="divider" style="left:315px"></div>
  <div class="f-col" style="left:339px">
    <h4>POPULAR SEARCHES</h4>
    <ul><li>Engagement</li><li>Charms</li><li>Rings</li><li>Earings</li><li>View all</li></ul>
  </div>
  <div class="divider" style="left:499px"></div>
  <div class="f-col" style="left:533px">
    <h4>QUICK LINKS</h4>
    <div class="links">
      <ul><li>Engagement</li><li>Jewellery</li><li>Diamonds</li><li>Designers</li><li>Accessories</li><li>View all</li></ul>
      <ul><li>About Us</li><li>Wish List</li><li>My Accounts</li><li>Orders</li></ul>
    </div>
  </div>
  <div class="divider" style="left:733px"></div>
  <div class="f-col" style="left:782px">
    <h4>NEWSLETTER / SOCIAL MEDIA / PAYMENT</h4>
    <form class="news"><input type="text" value="Ihre E-Mail-Adresse" aria-label="Email"><button type="button" aria-label="Subscribe"><svg width="14" height="10" viewBox="0 0 14 10"><path d="M0 5h11M7 1l4 4-4 4" stroke="#fff" stroke-width="2" fill="none"/></svg></button></form>
    <div class="net"><span><i></i>Chatterly</span><span><i></i>quipster</span></div>
    <div class="pay">
      <span>Paywell</span><span>Checkly</span><span>Vira</span><span></span>
      <span style="font-size:9px">Vira Spark</span><span>Mintcard</span><span>Marlo</span><span class="badge"></span>
    </div>
  </div>
</footer>
</body>
</html>
```